Redesign of property flyer

I am working on the redevelopment of a shopping center and have created a brochure for the property using Microsoft Publisher. I would like to have a condensed version of the flyer created that is two pages and has a very modern, slick look. Any information that will go into the new flyer can be found either on the attached version or on the property's website: http://www.parcelvane.com/lid/40613827.

-Must be two pages
-Must have large photos using the attached renderings
-Must include my company's logo and contact information
-Can include stock images of shoppers and restaurants
-Should include a regional map of the shopping center's location

Shopping

• -Must be two pages
• -Must have large photos using the attached renderings
• -Must include my company's logo and contact information
• -Can include stock images of shoppers and restaurants
• -Should include a regional map of the shopping center's location
• -Should not have a lot of white, open space

```html
<!DOCTYPE html>
<html lang="en">
<head>
<meta charset="utf-8">
<title>Fairmarch Redevelopment – Two-Page Flyer</title>
<link rel="stylesheet" href="https://fonts.googleapis.com/css2?family=Roboto+Condensed:wght@400;700&family=Cardo:wght@400;700&display=swap">
<style>
:root{
  --stage:#3b2c22;
  --green-dark:#2f7a1f;
  --green:#4ea42e;
  --green-light:#8cc63f;
  --green-pale:#eef6d8;
  --ink:#2b2b2b;
  --ink-green:#24521a;
  --white:#ffffff;
  --red:#c8161d;
  --sky:#7fb2e4;
  --asphalt:#4a4d50;
}
*{box-sizing:border-box;margin:0;padding:0}
html,body{width:1200px;height:812px;overflow:hidden}
body{background:var(--stage);position:relative;font-family:"Roboto Condensed",Arial,sans-serif;color:var(--ink)}
.page{position:absolute;background:var(--white);overflow:hidden;box-shadow:0 4px 14px rgba(0,0,0,.45)}
.page--front{left:74px;top:57px;width:507px;height:682px}
.page--back{left:614px;top:57px;width:510px;height:684px}
.abs{position:absolute}

/* brand */
.brand{display:flex;align-items:center;gap:7px}
.brand__dot{width:30px;height:30px;border-radius:50%;flex:none}
.brand__name{font-family:"Cardo",Georgia,serif;font-weight:400;font-size:19px;line-height:1}
.brand__tag{font-family:"Cardo",Georgia,serif;font-size:5.4px;letter-spacing:.4px;text-transform:uppercase;margin-top:2px}

/* front */
.front-header{left:0;top:0;width:507px;height:135px;background:linear-gradient(180deg,#6bb83a 0%,var(--green) 55%,#3f9128 100%)}
.front-header .brand{left:26px;top:26px;color:var(--white)}
.front-header .brand__dot{background:var(--white)}
.front-web{left:68px;top:90px;font-size:10.5px;font-weight:700;color:var(--white)}
.title{font-family:"Roboto Condensed",Arial,sans-serif;font-weight:700;font-size:28px;line-height:1.02}
.front-title{left:240px;top:20px;color:var(--white);text-shadow:0 1px 2px rgba(0,0,0,.3)}
.front-address{left:240px;top:90px;font-size:12px;font-weight:700;color:var(--white)}
.photo{background:linear-gradient(180deg,var(--sky) 0%,#c9dff0 30%,#a9a98e 44%,var(--asphalt) 62%,#5b6a45 100%)}
.front-photo{left:0;top:120px;width:507px;height:220px}
.photo-edge{left:0;width:100%}
.badge{left:232px;top:286px;width:106px;height:64px;border-radius:50%;background:radial-gradient(circle at 40% 35%,#e83a2e,var(--red) 60%,#8c0d12);transform:rotate(22deg);border:2px solid #fff;display:flex;align-items:center;justify-content:center;text-align:center;color:var(--white);font-weight:700;font-size:11px;line-height:1.05;text-transform:uppercase}
.badge span{transform:rotate(0deg)}
.front-lower{left:0;top:335px;width:507px;height:347px;background:linear-gradient(180deg,#fbfdf4 0%,var(--green-pale) 45%,#c7e08c 100%)}
.lease{left:40px;top:340px;font-family:"Cardo",Georgia,serif;font-weight:700;font-size:21px;color:var(--ink-green)}
.map{left:34px;top:415px;width:189px;height:176px;border-radius:8px;border:2px solid #fff;background:linear-gradient(135deg,#6f7a5a,#8e8f80 45%,#5d6b4c);box-shadow:0 1px 4px rgba(0,0,0,.3)}
.callbox{left:26px;top:597px;width:205px;height:70px;background:var(--green-dark);border-radius:10px;text-align:center;color:var(--white)}
.callbox__phone{font-size:17px;font-weight:700;margin-top:4px}
.callbox__phone small{font-size:12px;font-weight:400}
.callbox__web{margin:5px auto 0;width:185px;height:30px;border-radius:7px;background:var(--white);color:var(--ink);font-weight:700;font-size:14px;line-height:30px}
.highlights{left:266px;top:398px;width:230px}
.highlights h2{font-family:"Cardo",Georgia,serif;font-weight:700;font-size:19px;color:var(--ink);margin-bottom:5px}
.highlights ul{list-style:none}
.highlights li{display:flex;gap:5px;font-size:10.3px;line-height:12.5px;margin-bottom:5px}
.tick{flex:none;width:10px;height:10px;margin-top:1px}
.contacts{left:266px;top:610px;width:241px;font-size:10px;line-height:12px}
.contacts .person{border-top:1px solid #8a9a6a;padding:4px 0 3px}
.contacts b{font-size:11px}

/* back */
.back-header .brand{left:24px;top:20px;color:var(--green-dark)}
.back-header .brand__dot{background:var(--green)}
.back-title{left:200px;top:18px;color:var(--green)}
.back-address{left:200px;top:50px;font-size:12.5px;color:var(--ink)}
.contact-row{left:115px;top:84px;display:flex;align-items:center;gap:8px;font-size:8px;line-height:10px}
.contact-row__label{font-family:"Cardo",Georgia,serif;font-size:20px;color:var(--green-dark);padding-right:8px;border-right:1px solid #999}
.contact-row .person+.person{border-left:1px solid #999;padding-left:8px}
.contact-row b{color:var(--green-dark)}
.back-photo-top{left:0;top:125px;width:510px;height:275px}
.back-web{left:20px;top:398px;font-family:"Cardo",Georgia,serif;font-weight:700;font-size:17px;letter-spacing:4.6px;color:var(--ink)}
.back-photo-bottom{left:0;top:433px;width:510px;height:251px}
</style>
</head>
<body>

<section class="page page--front" aria-label="Flyer front">
  <header class="abs front-header">
    <div class="abs brand">
      <span class="brand__dot"></span>
      <div><div class="brand__name">Hollis-Pryor</div><div class="brand__tag">Real Estate, LLC · Commercial Brokerage</div></div>
    </div>
    <div class="abs front-web">www.HollisPryorRE.com</div>
    <h1 class="abs title front-title">Fairmarch<br>Redevelopment</h1>
    <div class="abs front-address">2740 Calder Rd, Brenton, NC 28990</div>
  </header>
  <div class="abs photo front-photo" role="img" aria-label="Aerial rendering of the redeveloped shopping center with parking lot and storefronts"></div>
  <svg class="abs photo-edge" style="top:108px" width="507" height="24" viewBox="0 0 507 24" aria-hidden="true">
    <path d="M0 0H507V10H335Q318 10 306 22H104Q92 10 75 10H0Z" fill="#3f9128"/>
    <path d="M0 10H75Q92 10 104 22H306Q318 10 335 10H507V24H0Z" fill="none"/>
  </svg>
  <div class="abs front-lower"></div>
  <svg class="abs photo-edge" style="top:322px" width="507" height="70" viewBox="0 0 507 70" aria-hidden="true">
    <path d="M0 18Q150 0 260 20T507 8V70H0Z" fill="#8cc63f"/>
    <path d="M0 26Q160 6 270 28T507 18V70H0Z" fill="#ffffff"/>
    <path d="M230 70Q360 40 507 46V70Z" fill="#cfe6a0"/>
  </svg>
  <div class="abs badge"><span>Under New<br>Ownership &amp;<br>Management</span></div>
  <div class="abs lease">Available for Lease</div>
  <div class="abs map" role="img" aria-label="Regional aerial map marking the site location"></div>
  <div class="abs callbox">
    <div class="callbox__phone">(555) 014-2290 <small>(Office)</small></div>
    <div class="callbox__web">www.HollisPryorRE.com</div>
  </div>
  <div class="abs highlights">
    <h2>Property Highlights</h2>
    <ul>
      <li><svg class="tick" viewBox="0 0 10 10"><rect width="10" height="10" fill="#4ea42e"/><path d="M2 5l2 2 4-5" stroke="#fff" stroke-width="1.6" fill="none"/></svg><span>Anchors: 15-screen Starline Cinema, Ridgeway Outdoors, and Voltmart</span></li>
      <li><svg class="tick" viewBox="0 0 10 10"><rect width="10" height="10" fill="#4ea42e"/><path d="M2 5l2 2 4-5" stroke="#fff" stroke-width="1.6" fill="none"/></svg><span>Spaces from 1,887 SF - 22,833 SF</span></li>
      <li><svg class="tick" viewBox="0 0 10 10"><rect width="10" height="10" fill="#4ea42e"/><path d="M2 5l2 2 4-5" stroke="#fff" stroke-width="1.6" fill="none"/></svg><span>Prime location adjacent from Kestrel's successful Willow Run Mall</span></li>
      <li><svg class="tick" viewBox="0 0 10 10"><rect width="10" height="10" fill="#4ea42e"/><path d="M2 5l2 2 4-5" stroke="#fff" stroke-width="1.6" fill="none"/></svg><span>Less than 10 minutes from Fort Alder</span></li>
      <li><svg class="tick" viewBox="0 0 10 10"><rect width="10" height="10" fill="#4ea42e"/><path d="M2 5l2 2 4-5" stroke="#fff" stroke-width="1.6" fill="none"/></svg><span>49,000 vehicles per day on Calder Rd</span></li>
      <li><svg class="tick" viewBox="0 0 10 10"><rect width="10" height="10" fill="#4ea42e"/><path d="M2 5l2 2 4-5" stroke="#fff" stroke-width="1.6" fill="none"/></svg><span>Population (10 mi): 300,740</span></li>
      <li><svg class="tick" viewBox="0 0 10 10"><rect width="10" height="10" fill="#4ea42e"/><path d="M2 5l2 2 4-5" stroke="#fff" stroke-width="1.6" fill="none"/></svg><span>Average HH Income (10 mi): $51,889</span></li>
      <li><svg class="tick" viewBox="0 0 10 10"><rect width="10" height="10" fill="#4ea42e"/><path d="M2 5l2 2 4-5" stroke="#fff" stroke-width="1.6" fill="none"/></svg><span># of Households (10 mi): 127,254</span></li>
      <li><svg class="tick" viewBox="0 0 10 10"><rect width="10" height="10" fill="#4ea42e"/><path d="M2 5l2 2 4-5" stroke="#fff" stroke-width="1.6" fill="none"/></svg><span>Expected Delivery: Q1 2014</span></li>
    </ul>
  </div>
  <div class="abs contacts">
    <div class="person"><b>Owen Hollis,</b> (555) 014-7731 (Cell)<br>Email: owen@hollispryorre.com</div>
    <div class="person"><b>Grady Pryor, CCIM, CLS,</b> (555) 014-6608 (Cell)<br>Email: grady@hollispryorre.com</div>
  </div>
</section>

<section class="page page--back" aria-label="Flyer back">
  <header class="back-header">
    <div class="abs brand">
      <span class="brand__dot"></span>
      <div><div class="brand__name">Hollis-Pryor</div><div class="brand__tag">Real Estate, LLC · Commercial Brokerage</div></div>
    </div>
    <h1 class="abs title back-title">Fairmarch Redevelopment</h1>
    <div class="abs back-address">2740 Calder Rd, Brenton, NC 28990</div>
    <div class="abs contact-row">
      <span class="contact-row__label">Contact</span>
      <div class="person"><b>Grady Pryor, CCIM, CLS,</b> (555) 014-6608 <b>(Cell)</b><br><b>Email:</b> grady@hollispryorre.com</div>
      <div class="person"><b>Owen Hollis,</b> (555) 014-7731 <b>(Cell)</b><br><b>Email:</b> owen@hollispryorre.com</div>
    </div>
  </header>
  <div class="abs photo back-photo-top" role="img" aria-label="Street-level rendering of storefronts, pylon sign and parking under a blue sky"></div>
  <svg class="abs photo-edge" style="top:113px" width="510" height="16" viewBox="0 0 510 16" aria-hidden="true">
    <path d="M0 4H90Q105 4 118 14H510V16H0Z" fill="#4ea42e"/>
    <path d="M118 10H510V14H118Z" fill="#8cc63f"/>
  </svg>
  <div class="abs" style="left:0;top:398px;width:510px;height:36px;background:#fff"></div>
  <div class="abs back-web">www.HollisPryorRE.com</div>
  <svg class="abs photo-edge" style="top:420px" width="510" height="16" viewBox="0 0 510 16" aria-hidden="true">
    <path d="M0 12H380Q395 12 408 2H510V16H0Z" fill="#4ea42e"/>
    <path d="M0 14H510V16H0Z" fill="#8cc63f"/>
  </svg>
  <div class="abs photo back-photo-bottom" role="img" aria-label="Rendering of the shopping center corner building with landscaped median and flower beds"></div>
</section>

</body>
</html>
```